Modern Medical Optometry Website

We need mordern, Patient friendly website. Easy to navigate and enhance our advance medical technology and excellent patient care.
1. HOME PAGE
2. OUR TEAM PAGE
3. EYECARE PAGE - VISION SERVICES, EYE EXAMS, KERATOCONUS CENTER, GLAUCOMA , DIABITES, VELMORIN EXAM, DIGITAL RETINAL, OCT.
4. MYOPIA CONTROL CLINIC
5. DRY EYE CLINIC
6. EYEWEAR
7. PATIENT CENTER - BLOG
7. CONTACT US
This is our current website www.lumvarta.com
and We want to add more content and a cleaner design like these website
http://norvellbrookclinic.com/
https://www.tqvamori.com/

```html
<!DOCTYPE html>
<html lang="en">
<head>
<meta charset="utf-8">
<title>Lumvarta Optometry</title>
<link rel="stylesheet" href="https://fonts.googleapis.com/css2?family=Ubuntu:wght@300;400;500;700&family=Roboto:wght@400;500&display=swap">
<style>
:root{
  --blue:#1e7fc0;--blue-dark:#0f679e;--blue-mid:#1573ad;--blue-light:#1b80ba;
  --stripe:#3a9ad6;--ink:#2b2b2b;--muted:#666;--link:#1a5f97;
  --orange:#e8801f;--gold:#f2b51c;--green:#22a33a;--gray:#dfe0e2;--bar:#efefef;
}
*{box-sizing:border-box;margin:0;padding:0}
html,body{width:1200px;height:1200px;overflow:hidden;background:#fff}
body{position:relative;font-family:"Ubuntu",sans-serif;color:var(--ink)}
.abs{position:absolute}
.topbar{left:0;top:0;width:1200px;height:33px;background:var(--bar)}
.pill{top:8px;height:19px;border-radius:2px;font-size:9px;display:flex;align-items:center;gap:5px;padding:0 7px;font-weight:500}
.pill.phone{left:738px;width:99px;background:var(--gold);color:#222}
.pill.book{left:843px;width:121px;background:var(--orange);color:#fff}
.social{top:10px;width:14px;height:14px;border-radius:50%;background:#9aa3ad}
.lang{left:1069px;top:8px;width:99px;height:19px;background:#fff;border:1px solid #d4d4d4;font-size:9px;color:#555;display:flex;align-items:center;padding-left:6px;gap:5px}
.lang i{width:10px;height:7px;background:#b9c3cf;display:block}
.lang b{margin-left:auto;margin-right:6px;font-size:7px;font-weight:400}
.brand{left:30px;top:40px;display:flex;flex-direction:column;align-items:center;gap:3px}
.brand .sq{width:20px;height:20px;background:var(--gold)}
.brand span{font-size:11px;color:#333;letter-spacing:.5px;line-height:1}
.brand small{font-size:6.5px;color:#333;letter-spacing:1px;margin-top:-2px}
.nav{top:59px;font-family:"Roboto",sans-serif;font-size:10.5px;color:#222;white-space:nowrap}
.nav.active{color:var(--blue)}
.hero{left:0;top:96px;width:1200px;height:417px;background:linear-gradient(100deg,#c9c2bb 0%,#b9a594 30%,#8d8c93 55%,#9ea0a8 100%)}
.dropdown{left:613px;top:96px;width:121px;height:140px;background:#ececec;padding-top:8px;font-family:"Ubuntu",sans-serif}
.dropdown li{list-style:none;font-size:8.6px;color:#555;height:18.8px;padding-left:6px;display:flex;align-items:center;gap:5px;white-space:nowrap}
.dropdown li:before{content:"";border-left:4px solid #888;border-top:2.5px solid transparent;border-bottom:2.5px solid transparent}
.hero-title{left:552px;top:280px;font-size:39px;line-height:46px;font-weight:700;color:#fff;letter-spacing:.5px;white-space:nowrap}
.hero-sub{left:555px;top:387px;width:480px;font-size:14.5px;line-height:22.5px;color:#fff;font-weight:400}
.arrow{top:286px;width:32px;height:32px;border:2px solid #fff;border-radius:50%}
.dot{top:492px;width:7px;height:7px;background:#3c4550}
.band{left:0;top:513px;width:1200px;height:270px;background:var(--gray)}
.panel{top:509px;height:274px;color:#fff}
.panel h2{font-size:15.5px;font-weight:400;position:absolute;top:40px}
.p1{left:160px;width:291px;background:var(--blue-dark)}
.p2{left:451px;width:300px;background:var(--blue-mid)}
.p3{left:751px;width:292px;background:var(--blue-light)}
.txt{font-size:10.3px;line-height:15.5px}
.row{display:flex;align-items:center;gap:9px;font-size:8.7px;font-weight:500;height:15.5px}
.row svg{width:10px;height:10px}
.sundays{left:515px;top:640px;width:168px;height:30px;border:1.5px solid #fff;border-radius:3px;font-size:11px;font-weight:500;display:flex;align-items:center;justify-content:center}
.appt{left:836px;top:718px;width:139px;height:28px;background:var(--green);border-radius:2px;font-size:10px;font-weight:500;display:flex;align-items:center;justify-content:center;gap:8px}
.welcome{left:163px;top:826px;width:410px;text-align:center;font-size:19.5px;color:var(--link)}
.body{left:163px;width:412px;font-size:9.8px;line-height:18.7px;color:#555;font-weight:300}
.svc{font-size:9.8px;color:var(--link)}
.btn{left:297px;top:1130px;width:124px;height:29px;background:var(--orange);color:#fff;border-radius:2px;font-size:10px;display:flex;align-items:center;justify-content:center}
.tile{overflow:hidden}
.tile span{position:absolute;left:18px;bottom:20px;color:#fff;font-size:15px;font-weight:500}
</style>
</head>
<body>
<div class="abs topbar"></div>
<div class="abs pill phone">
  <svg width="10" height="10" viewBox="0 0 10 10"><rect width="10" height="10" rx="1" fill="#222"/><path d="M3 2.5l1 1.5-.6.7a4 4 0 0 0 1.9 1.9l.7-.6 1.5 1-.5 1A5 5 0 0 1 2 3z" fill="#f2b51c"/></svg>555-210-4830</div>
<div class="abs pill book">
  <svg width="9" height="9" viewBox="0 0 9 9"><rect x=".5" y="1.5" width="8" height="7" fill="none" stroke="#fff"/><path d="M.5 3.5h8" stroke="#fff"/></svg>Make An Appointment</div>
<div class="abs social" style="left:978px"></div>
<div class="abs social" style="left:999px"></div>
<div class="abs social" style="left:1020px"></div>
<div class="abs social" style="left:1041px"></div>
<div class="abs lang"><i></i>English<b>▼</b></div>

<div class="abs brand"><div class="sq"></div><span>LUMVARTA</span><small>OPTOMETRY</small></div>
<div class="abs nav active" style="left:480px">HOME</div>
<div class="abs nav" style="left:537px">OUR TEAM</div>
<div class="abs nav" style="left:615px">EYECARE <span style="font-size:7px;color:var(--blue)">▼</span></div>
<div class="abs nav" style="left:685px">MYOPIA CONTROL CLINIC</div>
<div class="abs nav" style="left:831px">DRY EYE CLINIC</div>
<div class="abs nav" style="left:930px">EYEWEAR</div>
<div class="abs nav" style="left:1004px">PATIENT CENTER</div>
<div class="abs nav" style="left:1109px">CONTACT US</div>

<div class="abs hero" role="img" aria-label="Mother and smiling daughter at an eye exam beside optical equipment"></div>
<ul class="abs dropdown">
  <li>VISION SERVICES</li><li>EYE EXAMS</li><li>KERATOCONUS CENTER</li><li>GLAUCOMA</li><li>DIABITES</li><li>VELMORIN EXAM</li><li>DIGITAL RETINAL OCT.</li>
</ul>
<h1 class="abs hero-title">THE LUMVARTA<br>PROMISE</h1>
<p class="abs hero-sub">We take great pride in providing you with state-of-the-art eyecare matched with personal attention from our staff and doctors.</p>
<div class="abs arrow" style="left:81px"><svg width="28" height="28" viewBox="0 0 28 28"><path d="M16 9l-5 5 5 5" fill="none" stroke="#fff" stroke-width="1.5"/></svg></div>
<div class="abs arrow" style="left:1083px"><svg width="28" height="28" viewBox="0 0 28 28"><path d="M12 9l5 5-5 5" fill="none" stroke="#fff" stroke-width="1.5"/></svg></div>
<div class="abs dot" style="left:585px;background:#7fc3ee;border:1px solid #fff"></div>
<div class="abs dot" style="left:598px"></div>
<div class="abs dot" style="left:611px"></div>

<div class="abs band"></div>
<div class="abs panel p1">
  <h2 style="left:13px">Clinic Location</h2>
  <svg class="abs" style="left:252px;top:34px" width="20" height="22" viewBox="0 0 20 22"><path d="M10 2a5 5 0 0 1 5 5c0 4-5 9-5 9S5 11 5 7a5 5 0 0 1 5-5z" fill="none" stroke="#fff" stroke-width="1.5"/><circle cx="10" cy="7" r="1.8" fill="#fff"/><path d="M3 18h14" stroke="#fff" stroke-width="1.5"/></svg>
  <div class="abs txt" style="left:26px;top:73px">4820 Calloway Ave,<br>Dunmere, CA 90412</div>
  <div class="abs" style="left:26px;top:110px">
    <div class="row"><svg viewBox="0 0 10 10"><path d="M1 4q4-3 8 0v2H7V5H3v1H1zM2 7h6v2H2z" fill="#fff"/></svg>555-210-4830</div>
    <div class="row"><svg viewBox="0 0 10 10"><path d="M3 1h4v3H3zM1 4h8v4H1zM3 7h4v2H3z" fill="#fff"/></svg>555-210-4871</div>
    <div class="row"><svg viewBox="0 0 10 10"><rect x="0" y="2" width="10" height="6" fill="#fff"/><path d="M0 2l5 3 5-3" fill="none" stroke="#0f679e"/></svg>info@lumvarta.com</div>
  </div>
  <div class="abs txt" style="left:150px;top:73px">2291 Harlow St.,<br>Suite 4,<br>Westbrook, CA 90418</div>
  <div class="abs" style="left:150px;top:131px">
    <div class="row"><svg viewBox="0 0 10 10"><path d="M3 1h4v3H3zM1 4h8v4H1zM3 7h4v2H3z" fill="#fff"/></svg>555-318-6620</div>
    <div class="row" style="margin-top:1px"><svg viewBox="0 0 10 10"><rect x="0" y="2" width="10" height="6" fill="#fff"/><path d="M0 2l5 3 5-3" fill="none" stroke="#0f679e"/></svg>westbrook@lumvarta.com</div>
  </div>
</div>
<div class="abs panel p2">
  <h2 style="left:21px">Operating Hours</h2>
  <svg class="abs" style="left:262px;top:34px" width="22" height="22" viewBox="0 0 22 22"><path d="M18 8A8 8 0 1 0 19 13" fill="none" stroke="#fff" stroke-width="1.6"/><path d="M19 4v4h-4" fill="none" stroke="#fff" stroke-width="1.6"/><path d="M11 6v5l3 2" fill="none" stroke="#fff" stroke-width="1.6"/></svg>
  <div class="abs txt" style="left:34px;top:72px;font-size:11.2px">Monday - Thursday<br>Friday<br>Saturday</div>
  <div class="abs txt" style="left:172px;top:72px;font-size:11.2px">9 am - 6 pm<br>8.30 am - 5 pm<br>8.30 am- 5 pm</div>
  <div class="abs txt" style="left:0;top:177px;width:300px;text-align:center;font-size:11px">Please keep in mind<br>we are closed for lunch 1-2 pm</div>
</div>
<div class="abs sundays" style="color:#fff">CLOSED ON SUNDAYS</div>
<div class="abs panel p3">
  <h2 style="left:22px">Book an appointment</h2>
  <svg class="abs" style="left:248px;top:36px" width="22" height="22" viewBox="0 0 22 22"><rect x="2" y="4" width="18" height="16" fill="none" stroke="#fff" stroke-width="1.5"/><path d="M2 8h18M6 2v4M16 2v4" stroke="#fff" stroke-width="1.5"/><g fill="#fff"><rect x="5" y="11" width="2" height="2"/><rect x="10" y="11" width="2" height="2"/><rect x="15" y="11" width="2" height="2"/><rect x="5" y="15" width="2" height="2"/><rect x="10" y="15" width="2" height="2"/></g></svg>
  <div class="abs" style="left:30px;top:71px;font-size:11.2px;font-weight:500">Specialties</div>
  <div class="abs txt" style="left:30px;top:87px;color:#cfe6f5">Optometrist</div>
  <div class="abs" style="left:30px;top:117px;font-size:11.2px;font-weight:500">In-Network Insurances</div>
  <div class="abs txt" style="left:30px;top:133px;color:#cfe6f5">Corvena Health<br>Halvern Care<br>Halvern Care Plus Shield</div>
  <div class="abs" style="left:30px;top:183px;font-size:8.5px;text-decoration:underline;font-weight:500">View all</div>
</div>
<div class="abs appt" style="color:#fff"><svg width="10" height="10" viewBox="0 0 10 10"><rect x=".5" y="1.5" width="9" height="8" fill="none" stroke="#fff"/><path d="M.5 4h9" stroke="#fff"/></svg>Make An Appointment</div>

<h2 class="abs welcome" style="font-weight:400">Welcome to Lumvarta Optometry</h2>
<p class="abs body" style="top:869px">Welcome to Lumvarta Optometry, where your vision and eye health are our sole priority. We take great pride in providing you with state-of-the-art eyecare matched with personal attention from our staff and doctors. Your quality of life is our goal and we believe that healthy eyesight is vital to achieving it.</p>
<p class="abs body" style="top:955px">Our professional and personable staff is highly trained in helping you achieve and maintain healthy eyesight. Our optometrists have combined experiences and specialize in Orthokeratology (OrthoK), Ocular disease, Glaucoma diagnosis &amp; management.</p>
<div class="abs svc" style="left:165px;top:1041px">Comprehensive Eye Examinations</div>
<div class="abs svc" style="left:165px;top:1064px">Contact Lenses</div>
<div class="abs svc" style="left:165px;top:1086px">Eye Infections, Eye Injuries, Dry Eyes</div>
<div class="abs svc" style="left:377px;top:1040px">Retinal Camera</div>
<div class="abs svc" style="left:377px;top:1062px">Eye Diseases; Cataracts, Glaucoma</div>
<div class="abs svc" style="left:377px;top:1085px">Diabetic Screenings</div>
<div class="abs btn">View all our services</div>

<div class="abs tile" style="left:667px;top:783px;width:235px;height:207px;background:linear-gradient(160deg,#6b6458,#3e4a55 55%,#5d5447)" role="img" aria-label="Close-up of an eye with cracked dry texture"><span>Dry Eyes</span></div>
<div class="abs tile" style="left:902px;top:783px;width:298px;height:249px;background:linear-gradient(150deg,#c9b3ad,#b89d96 50%,#9d8e92)" role="img" aria-label="Fingertip holding a contact lens">
  <div class="abs" style="left:11px;top:11px;width:280px;height:225px;background:rgba(255,255,255,.22)"></div>
  <svg class="abs" style="left:141px;top:116px" width="14" height="14" viewBox="0 0 14 14"><path d="M7 0v14M0 7h14" stroke="#fff" stroke-width="2"/></svg>
  <span style="bottom:25px">Contact Lenses</span></div>
<div class="abs tile" style="left:609px;top:990px;width:293px;height:210px;background:linear-gradient(180deg,#7d8368,#4f5a66 60%,#3a4450)" role="img" aria-label="Group photo of the clinic team"><span style="bottom:18px">Best Team</span></div>
<div class="abs tile" style="left:902px;top:1032px;width:298px;height:168px;background:linear-gradient(160deg,#5c4d45,#3d3836 60%,#4a3f3a)" role="img" aria-label="Child wearing a trial frame during an eye examination"><span style="bottom:20px">Comprehensive Eye Examinations</span></div>
</body>
</html>
```